Door Hanger General Contractor

design high quality marketing piece to promote our general contractor business.
Use all content create badges, banners, bubbles, boxes ect to highlight text.
Template format is uploaded in images
Make font as large as possible, minimize negative space, fill areas
FRONT SIDE
Your Neighbor Just Remodeled
Come See Our Work at:
(under this create blank white box placeholder for address)
LOVE YOUR HOME AGAIN!
WE MAKE REMODELING EASY
FREE 3D DESIGN SERVICES
FREE ESTIMATES
LICENSED GENERAL CONTRACTORS
We Specialize in:
Kitchen Remodel
Bathroom Remodel
Interior/Exterior Painting
Flooring: Carpet, Vinyl, Wood & Tile
Energy Efficient Upgrades
Window/Door Replacement
WATER & MOLD DAMAGE
BACK SIDE
GET STARTED IN 3 SIMPLE STEPS:
1 ORDER FREE ESTIMATE & DESIGN
2 APPROVE ESTIMATE & DESIGN
3 HEARTHWAY RENOVATORS BUILDS YOUR DREAM
Thinking About Selling?
We Buy Homes
GET CASH OFFER
SELLING MADE EASY
CALL NOW!!
Hearthway Renovators Inc.
858-555-0174 Call/Text
BrightGableHomes.example
CSLB# 4087261
home owners
General Contractor

```html
<!DOCTYPE html>
<html lang="en">
<head>
<meta charset="utf-8">
<title>Hearthway Renovators Door Hanger</title>
<link href="https://fonts.googleapis.com/css2?family=League+Gothic&family=Open+Sans:wght@600&display=swap" rel="stylesheet">
<style>
  :root {
    --ink: #000000;
    --paper: #ffffff;
    --brand-blue: #468bf0;
    --photo-warm: #c9b79c;
    --photo-paint: #4a4640;
    --photo-room: #d8d6d2;
    --photo-house: #a7b58f;
    --photo-sign: #9a6a5a;
  }
  * { margin: 0; padding: 0; box-sizing: border-box; }
  html, body { width: 1200px; height: 1200px; overflow: hidden; background: var(--paper); }
  .canvas { position: relative; width: 1200px; height: 1200px; }
  .hanger {
    position: absolute; top: 83px; width: 409px; height: 1034px;
    background: var(--ink); overflow: hidden;
    font-family: "League Gothic", "Arial Narrow", sans-serif;
  }
  .hanger--front { left: 115px; }
  .hanger--back { left: 676px; }
  .door-hole {
    position: absolute; left: 76px; top: 43px; width: 257px; height: 207px;
    background: var(--paper);
    border-radius: 128px 128px 0 0 / 100px 100px 0 0;
  }
  .line {
    position: absolute; left: 0; width: 100%; text-align: center;
    line-height: 1; transform: translateY(-50%); white-space: nowrap;
  }
  .headline { font-size: 42px; color: var(--brand-blue); }
  .brand-name { font-size: 36px; color: var(--paper); letter-spacing: 1px; }
  .address-box {
    position: absolute; left: 46px; top: 566px; width: 317px; height: 55px;
    background: var(--paper);
  }
  .photo-strip { position: absolute; left: 0; width: 100%; display: flex; }
  .photo { height: 100%; }
  .photo--kitchen { width: 137px; background: linear-gradient(135deg, var(--photo-warm), #eeeae4); }
  .photo--paint { width: 135px; background: radial-gradient(circle at 50% 50%, #8a6a40, var(--photo-paint)); }
  .photo--room { width: 137px; background: linear-gradient(180deg, #f0efec, var(--photo-room)); }
  .photo--inspection { width: 204px; background: linear-gradient(160deg, #c9cfd6, var(--photo-house)); }
  .photo--sold { width: 205px; background: linear-gradient(160deg, #7d9ac4, var(--photo-sign)); }
  .info-band {
    position: absolute; left: 0; top: 831px; width: 100%; height: 203px;
    background: var(--brand-blue);
  }
  .band-title { font-size: 30px; color: var(--ink); }
  .band-footer { font-size: 34px; color: var(--ink); }
  .service {
    font-family: "Open Sans", Arial, sans-serif; font-weight: 600;
    font-size: 13.5px; color: var(--paper);
  }
  .step { font-size: 32px; color: var(--paper); }
  .step-number { color: var(--brand-blue); }
  .offer { font-size: 32px; color: var(--paper); }
  .call-badge {
    position: absolute; left: 137px; top: 840px; width: 134px; height: 45px;
    background: var(--ink); border-radius: 14px;
    color: var(--paper); font-size: 38px; line-height: 46px; text-align: center;
  }
  .contact { font-size: 38px; color: var(--paper); }
  .license {
    font-family: "Open Sans", Arial, sans-serif; font-weight: 600;
    font-size: 12.5px; color: var(--paper);
  }
</style>
</head>
<body>
<div class="canvas">

  <section class="hanger hanger--front">
    <div class="door-hole"></div>
    <div class="line brand-name" style="top:420px">HEARTHWAY RENOVATORS</div>
    <div class="line headline" style="top:469px">YOUR NEIGHBOR</div>
    <div class="line headline" style="top:504px">JUST REMODELED</div>
    <div class="line headline" style="top:539px">COME SEE OUR WORK AT:</div>
    <div class="address-box"></div>
    <div class="line headline" style="top:659px">WE MAKE REMODELING EASY</div>
    <div class="line headline" style="top:694px">FREE 3D DESIGN SERVICES</div>
    <div class="line headline" style="top:729px">FREE ESTIMATES</div>
    <div class="photo-strip" style="top:763px;height:68px">
      <div class="photo photo--kitchen" role="img" aria-label="Kitchen remodel photo blended with a design sketch"></div>
      <div class="photo photo--paint" role="img" aria-label="Open paint cans with a brush and colour swatches"></div>
      <div class="photo photo--room" role="img" aria-label="Bright remodeled dining room interior"></div>
    </div>
    <div class="info-band">
      <div class="line band-title" style="top:22px">WE SPECIALIZE IN:</div>
      <div class="line service" style="top:42px">Kitchen Remodel</div>
      <div class="line service" style="top:57.5px">Bathroom Remodel</div>
      <div class="line service" style="top:73px">Interior/Exterior Painting</div>
      <div class="line service" style="top:88.5px">Flooring: Carpet, Vinyl, Wood &amp; Tile</div>
      <div class="line service" style="top:104px">Energy Efficient Upgrades</div>
      <div class="line service" style="top:119.5px">Window/Door Replacement</div>
      <div class="line service" style="top:135px">WATER &amp; MOLD DAMAGE</div>
      <div class="line band-footer" style="top:162px">LICENSED GENERAL CONTRACTORS</div>
    </div>
  </section>

  <section class="hanger hanger--back">
    <div class="door-hole"></div>
    <div class="photo-strip" style="top:289px;height:137px">
      <div class="photo photo--inspection" role="img" aria-label="Inspector with a clipboard in front of a house"></div>
      <div class="photo photo--sold" role="img" aria-label="Real estate sold sign in front of a home"></div>
    </div>
    <div class="line headline" style="top:482px;font-size:39px">GET STARTED IN 3 SIMPLE STEPS:</div>
    <div class="line step" style="top:531px"><span class="step-number">1</span> ORDER FREE ESTIMATE &amp; DESIGN</div>
    <div class="line step" style="top:562px"><span class="step-number">2</span> APPROVE ESTIMATE &amp; DESIGN</div>
    <div class="line step" style="top:592px"><span class="step-number">3</span> HEARTHWAY RENOVATORS BUILDS</div>
    <div class="line step" style="top:622px">YOUR DREAM</div>
    <div class="line headline" style="top:699px">THINKING ABOUT SELLING?</div>
    <div class="line offer" style="top:738px">We Buy Homes</div>
    <div class="line offer" style="top:768px">GET CASH OFFER</div>
    <div class="line offer" style="top:799px">SELLING MADE EASY</div>
    <div class="info-band"></div>
    <div class="call-badge">CALL NOW!!</div>
    <div class="line contact" style="top:904px">Hearthway Renovators Inc.</div>
    <div class="line contact" style="top:936px">858-555-0174 Call/Text</div>
    <div class="line contact" style="top:968px">BrightGableHomes.example</div>
    <div class="line license" style="top:995px">CSLB# 4087261</div>
  </section>

</div>
</body>
</html>
```